Need simple and modern looking business card with all my information on one side and logo on the other side
Info :
Company name - VELMAR CONSTRUCTION LLC
Company addres- 418 harbor 87th. Dunmoor park ny 10352
Email- velmarllc@tridomail.Com
Company phone number 555-318-6094
Cell number- 555-742-0583
Web site - velmarllc.Com
My name Gerald tomasino

Target Market(s)

Construction , home improvement, remodeling

Industry/Entity Type

Construction

Contact Information for Business Card

It has to be moder but at the same time simple

Font styles to use
Sans Serif

Colors
0255a3
ffffff
000000
f78f20
b1b1b1
9d9d9d
1b1b1b
33a6d7
ec1f27

Requirements
Must have
• My logo on one side maybe with a some kind of background on the other side all my information
Nice to have
• Some kind of background pictures provided by you .PLEASE HAVE ACCOUNT WITH PIXELVAULT WILL NOT PAY ANY EXTRA FEES .
Should not have
• Any kind of hamer, nails,screws, helmets itp. Please do not copy the other designs come up with something new.

```html
<!DOCTYPE html>
<html lang="en">
<head>
<meta charset="utf-8">
<title>Velmar Construction LLC – Business Card</title>
<link href="https://fonts.googleapis.com/css2?family=Lato:wght@300;400;700;900&display=swap" rel="stylesheet">
<style>
  :root {
    --brand-blue: #0255a3;
    --card-blue: #3a63a8;
    --white: #ffffff;
    --black: #000000;
    --ink: #1b1b1b;
    --orange: #f78f20;
    --star-grey: #c4c4c4;
    --sky: #33a6d7;
    --web-blue: #1f5ca8;
    --stage: #ecebe8;
  }
  * { margin: 0; padding: 0; box-sizing: border-box; }
  html, body { width: 1200px; height: 1000px; overflow: hidden; }
  body {
    background: var(--stage);
    font-family: "Lato", Arial, sans-serif;
    position: relative;
  }
  .card {
    position: absolute;
    width: 682px;
    height: 387px;
    background: var(--card-blue);
    overflow: hidden;
    box-shadow: 0 4px 10px rgba(0,0,0,0.25);
  }
  .card--front { left: 255px; top: 85px; }
  .card--back { left: 256px; top: 550px; border: 2px solid #14243f; }
  .card svg.shape { position: absolute; left: 0; top: 0; }

  .company-name {
    position: absolute;
    right: 46px; top: 32px;
    font-weight: 700; font-size: 23px;
    color: var(--black);
    letter-spacing: -0.3px;
  }
  .holder-name {
    position: absolute;
    font-weight: 300; font-size: 40px;
    color: var(--orange);
    -webkit-text-stroke: 0.6px var(--ink);
    line-height: 1;
  }
  .holder-name--first { left: 28px; top: 150px; }
  .holder-name--last { left: 115px; top: 204px; }
  .contact {
    position: absolute;
    font-weight: 700; font-size: 22px;
    color: var(--black);
    letter-spacing: -0.3px;
    white-space: nowrap;
  }
  .contact-phones { right: 58px; top: 192px; text-align: right; line-height: 31px; }
  .contact-phones .label { margin-right: 12px; }
  .contact-email { right: 72px; top: 287px; }
  .contact-address { right: 42px; top: 337px; }

  .brand {
    position: absolute;
    left: 148px; top: 175px;
    display: flex; align-items: center; gap: 12px;
  }
  .brand-mark { width: 26px; height: 26px; background: var(--orange); }
  .brand-name {
    font-weight: 900; font-size: 60px;
    color: var(--ink);
    letter-spacing: 4px;
    line-height: 1;
  }
  .website {
    position: absolute;
    left: 418px; top: 274px;
    font-weight: 700; font-size: 22px;
    color: var(--web-blue);
  }
</style>
</head>
<body>

<section class="card card--front" aria-label="Business card front">
  <svg class="shape" width="682" height="387" viewBox="0 0 682 387" aria-hidden="true">
    <polygon points="0,105 62,-20 95,-20 195,120 400,163 258,268 275,400 100,355 10,400 -10,400"
             fill="var(--star-grey)" stroke="var(--orange)" stroke-width="4"/>
  </svg>
  <div class="company-name">VELMAR CONSTRUCTION LLC</div>
  <div class="holder-name holder-name--first">Gerald</div>
  <div class="holder-name holder-name--last">Tomasino</div>
  <div class="contact contact-phones">
    <div><span class="label">Office</span>555-318-6094</div>
    <div><span class="label">CellPhone</span>555-742-0583</div>
  </div>
  <div class="contact contact-email">velmarllc@tridomail.com</div>
  <div class="contact contact-address">418 harbor 87th. Dunmoor park ny 10352</div>
</section>

<section class="card card--back" aria-label="Business card back">
  <svg class="shape" width="682" height="387" viewBox="0 0 682 387" aria-hidden="true">
    <path fill="var(--white)" d="
      M 60,88 L 90,78 L 100,62 L 150,70 L 175,50 L 205,60 L 230,42 L 262,40 L 278,10 L 285,35
      L 320,22 L 340,30 L 372,18 L 398,28 L 430,15 L 470,30 L 520,22 L 560,35 L 610,30 L 650,40
      L 672,60 L 660,95 L 648,125 L 660,160 L 675,200 L 682,230 L 682,387 L 510,387 L 495,365
      L 470,375 L 455,350 L 430,362 L 400,340 L 372,352 L 345,330 L 318,345 L 290,322 L 262,338
      L 240,318 L 212,330 L 190,310 L 165,326 L 140,305 L 118,318 L 100,290 L 88,300 L 92,262
      L 70,270 L 88,235 L 72,205 L 92,180 L 78,150 L 96,125 L 80,110 Z"/>
  </svg>
  <div class="brand">
    <span class="brand-mark" aria-hidden="true"></span>
    <span class="brand-name">VELMAR</span>
  </div>
  <div class="website">www.velmarllc.com</div>
</section>

</body>
</html>
```